Personal Vistrano Banner

I am creating a personal brand for myself. I want a vistrano banner that inspires and motivates people to reach their epic awesomeness. I am creating and designing my personal brand. It can be a background with words on a scenery a picture or 3d graphic. If someone looked at it, they should say it is aggressively epic and motivating. It should be dramatic and bold.
My personal goal is to help as many people reach financial freedom as possible, and challenge and break their own limiting beliefs. This personal brand will be integrated into my zomblat, quorVex, and professional vistrano fanpage (in addition to personal page). My goals are to open up a school for the underpriveleged children, develop my network marketing company team, and become a billionaire in the process. I want to attract people to me that really identify with doing what most think is impossible in terms of personal growth, impact to the world and financial wealth.
Updates

I have updated my brief with more background, and added a new comment to the discussion section to give you more to work with.

Reason: To give designers more time and to create a second and third place prize.

Reason: I am giving designers time to submit more designs

Target Market(s)

business professionals, and people with an entrepreneurial spirit.

Industry/Entity Type

Financial

Requirements
Must have
• It must be the exact dimensions required for vistrano banners. It should not be bigger or smaller. exact!!!

```html
<!DOCTYPE html>
<html lang="en">
<head>
<meta charset="utf-8">
<title>Dare to Dream Banner</title>
<link rel="stylesheet" href="https://fonts.googleapis.com/css2?family=Saira:wght@700;800&display=swap">
<style>
  :root {
    --page: #ffffff;
    --banner: #000000;
    --ink: #ffffff;
    --shadow: rgba(0, 0, 0, 0.55);
    --violet: #6a3f9a;
    --lilac: #b58fd8;
    --blue: #5a5fb8;
    --rose: #c86a8a;
    --amber: #e8a060;
  }
  html, body {
    margin: 0;
    padding: 0;
    width: 900px;
    height: 1200px;
    overflow: hidden;
    background: var(--page);
  }
  .canvas {
    position: relative;
    width: 900px;
    height: 1200px;
  }
  .banner {
    position: absolute;
    left: 25px;
    top: 444px;
    width: 850px;
    height: 314px;
    background: var(--banner);
    box-shadow: 6px 7px 5px var(--shadow);
    overflow: hidden;
    font-family: "Saira", "Arial Black", sans-serif;
    color: var(--ink);
  }
  .banner-art {
    position: absolute;
    inset: 0;
    background:
      radial-gradient(ellipse 110px 70px at 635px 80px, rgba(230, 225, 255, 0.85), transparent 70%),
      radial-gradient(ellipse 140px 110px at 470px 90px, rgba(181, 143, 216, 0.75), transparent 70%),
      radial-gradient(ellipse 200px 140px at 560px 180px, rgba(106, 63, 154, 0.85), transparent 70%),
      radial-gradient(ellipse 120px 120px at 700px 150px, rgba(90, 95, 184, 0.6), transparent 70%),
      radial-gradient(ellipse 120px 90px at 800px 260px, rgba(200, 106, 138, 0.65), transparent 70%),
      radial-gradient(ellipse 70px 90px at 255px 220px, rgba(232, 160, 96, 0.6), transparent 70%),
      radial-gradient(ellipse 90px 60px at 360px 290px, rgba(232, 160, 96, 0.45), transparent 70%),
      linear-gradient(90deg, transparent 0, transparent 280px, rgba(60, 30, 80, 0.4) 420px, rgba(60, 30, 80, 0.3) 100%);
  }
  .headline {
    position: absolute;
    left: 0;
    top: 0;
    margin: 0;
    font-weight: 800;
    line-height: 1;
  }
  .line {
    position: absolute;
    display: block;
    white-space: nowrap;
  }
  .line-dare { left: 14px; top: 28px; font-size: 86px; letter-spacing: -1px; }
  .line-dream { left: 16px; top: 110px; font-size: 40px; }
  .line-believe { left: 18px; top: 160px; font-size: 38px; font-weight: 700; }
  .line-can { left: 18px; top: 202px; font-size: 38px; font-weight: 700; }
  .line-achieve { left: 198px; top: 200px; font-size: 124px; letter-spacing: -1px; }
  .arrow {
    position: absolute;
    left: 26px;
    top: 262px;
    width: 72px;
    height: 36px;
  }
</style>
</head>
<body>
<main class="canvas">
  <section class="banner">
    <div class="banner-art" role="img" aria-label="Abstract cosmic burst of violet, blue, rose and amber light shards"></div>
    <h1 class="headline">
      <span class="line line-dare">DARE</span>
      <span class="line line-dream">TO DREAM</span>
      <span class="line line-believe">Believe</span>
      <span class="line line-can">You Can</span>
      <span class="line line-achieve">ACHIEVE</span>
    </h1>
    <svg class="arrow" viewBox="0 0 72 36" aria-hidden="true">
      <path d="M2 18 H66 M50 3 L67 18 L50 33" fill="none" stroke="#ffffff" stroke-width="4.5" stroke-linecap="square"/>
    </svg>
  </section>
</main>
</body>
</html>
```